Business card

We are looking for a creative person to deigns our company business card.

Target Market(s)

College age student

Industry/Entity Type

Accommodation

Contact Information for Business Card

We want a fun, clean and sophisticated design. It should look good, but more importantly the information should be legible.

Font styles to use
Serif
Sans Serif
Other font styles liked:
• Open Sans ,

Colors
33a6d7

Requirements
Must have
• Must have a young and memorable message. Be legible.
• Our logo on the back on a solid blue , please find color and logo attached
• LodgeBridgely.net on the back.
Nice to have
• I would like to have couple of different fonts on the LodgeBridgely.net on the back of the cards with a solid blue.

```html
<!DOCTYPE html>
<html lang="en">
<head>
<meta charset="utf-8">
<title>LodgeBridgely Business Card</title>
<link href="https://fonts.googleapis.com/css2?family=Open+Sans:wght@400;600;700&family=Roboto:wght@400;500&display=swap" rel="stylesheet">
<style>
  :root {
    --backdrop: #2b2b2d;
    --brand-blue: #3e96d4;
    --brand-navy: #0e5688;
    --navy-fold: #0a3d63;
    --paper: #ffffff;
    --ink: #1c1c1c;
  }
  * { box-sizing: border-box; margin: 0; padding: 0; }
  html, body { width: 1200px; height: 900px; overflow: hidden; }
  body {
    background: var(--backdrop);
    font-family: "Open Sans", sans-serif;
    position: relative;
  }
  .card {
    position: absolute;
    left: 280px;
    width: 640px;
    height: 366px;
    border-radius: 18px;
    overflow: hidden;
    box-shadow: 0 10px 24px rgba(0,0,0,0.45);
  }
  .card-back { top: 62px; background: var(--brand-blue); }
  .card-front { top: 472px; background: var(--paper); }

  .back-wordmark {
    position: absolute;
    inset: 0;
    display: flex;
    align-items: center;
    justify-content: center;
    color: var(--paper);
    font-weight: 700;
    font-size: 50px;
    letter-spacing: 0.5px;
  }

  .front-shapes { position: absolute; inset: 0; }

  .name-block {
    position: absolute;
    left: 330px;
    top: 60px;
    width: 290px;
    text-align: center;
    color: var(--paper);
    font-family: "Roboto", sans-serif;
  }
  .name-block .person { font-size: 22px; font-weight: 500; letter-spacing: 0.5px; }
  .name-block .role { font-size: 11px; letter-spacing: 0.5px; margin-top: 2px; }

  .brand {
    position: absolute;
    left: 44px;
    top: 78px;
    display: flex;
    align-items: center;
    gap: 10px;
    color: var(--brand-navy);
    font-weight: 700;
    font-size: 28px;
  }
  .brand-square { width: 22px; height: 22px; background: var(--brand-blue); }

  .contact-list {
    position: absolute;
    left: 44px;
    top: 182px;
    list-style: none;
    font-family: "Roboto", sans-serif;
    font-size: 17px;
    color: var(--ink);
  }
  .contact-list li { display: flex; align-items: center; gap: 12px; height: 32px; }
  .contact-icon { width: 24px; height: 24px; flex: none; }

  .address {
    position: absolute;
    right: 36px;
    bottom: 56px;
    width: 230px;
    text-align: center;
    color: var(--paper);
    font-family: "Roboto", sans-serif;
    font-size: 15px;
    line-height: 1.35;
  }
  .address svg { display: block; margin: 0 auto 6px; }
</style>
</head>
<body>

<section class="card card-back" aria-label="Card back">
  <p class="back-wordmark">LodgeBridgely.net</p>
</section>

<section class="card card-front" aria-label="Card front">
  <svg class="front-shapes" width="640" height="366" viewBox="0 0 640 366">
    <polygon points="330,0 640,0 640,366 400,366" fill="var(--brand-blue)"/>
    <polygon points="345,138 378,138 378,160" fill="var(--navy-fold)"/>
    <polygon points="330,52 620,52 620,138 345,138" fill="var(--brand-navy)"/>
  </svg>

  <div class="name-block">
    <p class="person">JOHN DOE</p>
    <p class="role">OWNER</p>
  </div>

  <div class="brand">
    <span class="brand-square"></span>
    <span>LodgeBridgely</span>
  </div>

  <ul class="contact-list">
    <li>
      <svg class="contact-icon" viewBox="0 0 24 24"><rect width="24" height="24" fill="var(--brand-blue)"/><path d="M7 5l3 3-1.5 2a9 9 0 0 0 5.5 5.5l2-1.5 3 3-2 2C11 19 5 13 5 7z" fill="#fff"/></svg>
      123-456-1234
    </li>
    <li>
      <svg class="contact-icon" viewBox="0 0 24 24"><rect width="24" height="24" fill="var(--brand-blue)"/><rect x="6" y="9" width="12" height="9" rx="1" fill="none" stroke="#fff" stroke-width="1.6"/><path d="M5 9c2-4 12-4 14 0" fill="none" stroke="#fff" stroke-width="1.6"/><circle cx="12" cy="13.5" r="2" fill="#fff"/></svg>
      123-456-1234
    </li>
    <li>
      <svg class="contact-icon" viewBox="0 0 24 24"><rect width="24" height="24" fill="var(--brand-blue)"/><rect x="5" y="7" width="14" height="10" fill="none" stroke="#fff" stroke-width="1.6"/><path d="M5 7l7 6 7-6" fill="none" stroke="#fff" stroke-width="1.6"/></svg>
      yourmail@email.com
    </li>
    <li>
      <svg class="contact-icon" viewBox="0 0 24 24"><rect width="24" height="24" fill="var(--brand-blue)"/><circle cx="12" cy="12" r="6.5" fill="none" stroke="#fff" stroke-width="1.6"/><path d="M5.5 12h13M12 5.5c-3 3.5-3 9.5 0 13M12 5.5c3 3.5 3 9.5 0 13" fill="none" stroke="#fff" stroke-width="1.2"/></svg>
      LodgeBridgely.net
    </li>
  </ul>

  <div class="address">
    <svg width="14" height="18" viewBox="0 0 14 18"><path d="M7 0a7 7 0 0 1 7 7c0 5-7 11-7 11S0 12 0 7a7 7 0 0 1 7-7z" fill="#fff"/><circle cx="7" cy="7" r="2.5" fill="var(--brand-blue)"/></svg>
    14830 - 124 Ave. full address<br>New York. ABC 123
  </div>
</section>

</body>
</html>
```